Professional WordPress Website Design & Development for IT Consulting Company (Trelvo)

We are an IT consulting company (Trelvo) based in Germany and are looking for a professional, modern and scalable WordPress website design INCLUDING full coding (WordPress theme/template).

IMPORTANT:
We do NOT want only a design (eg Photoshop files).
We want a fully working, coded WordPress website that we can host and manage ourselves.

The uploaded files (PowerPoint, HTML, logo) are ONLY for rough orientation.
They do NOT represent the final structure but give an idea of our visual style.

---

## COMPANY STRUCTURE (IMPORTANT)

Currently we operate as:

* Trelvo UG (limited liability)

Planned structure:

* Trelvo Operations GmbH (main operating company)
* Trelvo Holding GmbH
* optionally later: Trelvo Capital GmbH

The website should be designed as a scalable group website, but currently focus on the main brand "Trelvo".

---

## BUSINESS FOCUS (IMPORTANT)

Our main business is:
→ Managed Services (core focus)

Additional areas:

* IT Infrastructure (Nexorin, Valtek, Quadr-X)
* Fenestra Server/Client environments
* Cloud & Hybrid solutions
* Network, Firewall, VPN
* Data center operations, migrations and rollouts

The website should clearly communicate:
→ reliability, scalability, enterprise-level service quality

---

## DESIGN STYLE & VISUAL DIRECTION

We like the design direction from our uploaded PowerPoint.

IMPORTANT:

* We especially like the green checkered/grid-style background with dark/black gradient
* This style should be used as inspiration
* Colors: green + dark/black + modern IT style

Design should be:

* modern
* clean
* professional
* enterprise-level
* trustworthy
* not playful or overloaded

---

## TECHNICAL REQUIREMENTS

* WordPress (self-hosted)
* Full source code delivery (no proprietary lock-in)
* Custom theme or clean reusable theme
* Editable without developer
* Multilingual: German, English, Polish
* SEO-friendly
* Fast performance
* GDPR/DSVO compliant contact form

---

## RESPONSIVE DESIGN & ACCESSIBILITY

Must be optimized for:

* Desktop
* Tablet
* Mobile

Layout must adapt automatically.

Accessibility:

* Clear typography
* Good contrast
* Easy navigation
* Mobile-friendly usability

Mobile experience must be fully functional and professional.

---

## STRUCTURE (NO ONE-PAGE WEBSITE)

We want a structured website with pages and subpages.

MAIN NAVIGATION (HEADER):

* Home
* Managed Services (MAIN FOCUS)
* Services
* Solutions / Expertise
* Projects / News
* Resources
* Careers
* Company
* Contact

SUBNAVIGATION / SUBPAGES (examples):

Managed Services:

* Overview
* Service Models
* SLAs & Support
* Monitoring & Operations

Services:

* Nexorin
* Valtek
* Quadr-X
* Fenestra Server / Client
* PLDM / Ombrex
* Network / Firewall / VPN

Solutions:

* Data Center
* Cloud / Hybrid
* Migration Projects
* Security / Zero Trust

Projects / News:

* Projects
* Opportunities
* Articles

Resources:

* Available Experts
* Freelancer / Partner
* Internal Staff

Careers:

* Open Positions
* Freelancer Opportunities

Company:

* About Us
* Group Structure
* Values
* References

---

## HEADER / FOOTER STRUCTURE

HEADER:

* Sticky header (always visible)
* Main navigation with dropdowns or mega menu
* Clean, structured layout

FOOTER:

* Legal pages (Imprint, Privacy, Terms)
* Contact information
* Possibly quick links
* Consistent across all pages

---

## SPECIAL FEATURES

1. PROJECT / NEWS SYSTEM

* publish projects
* project opportunities
* articles

2. RESOURCE SYSTEM

* freelancers
* partners
* internal staff

With:

* skills
* availability
* role
* location
* language

---

## IMAGES, ICONS & LICENSING

Stock images (eg picVault) may be used as placeholders.

IMPORTANT:

* We will purchase final licenses ourselves
* No Zerlin images or unknown sources

Icons and illustrations are welcome but must be properly licensed.

At delivery:

* Full asset list required (images, icons, sources, licenses)

---

## DELIVERABLES

We expect:

* Fully working WordPress website
* Full source code
* Installation instructions
* Plugin list
* No hidden dependencies
* No forced subscriptions
* Full usage rights

---

## IMPORTANT

We want to pay ONCE and fully own everything.

---

## LANGUAGES

Content will be managed by us:

* German
* English
* Polish

---

## FILES

Uploaded files are only for inspiration.

---

We are looking for a long-term, scalable and professional solution suitable for enterprise customers.
Updates

Additional update regarding interactions, hover effects and animations:

HOVER EFFECTS

We would like to include subtle and modern hover effects across the website:

Cards (eg Open Positions, Projects): → slight green glow on hover → minimal lift effect (approx. 2–4px)

Navigation (header): → hover color should be green (NOT orange)

Footer links (Imprint, Privacy, Terms): → slightly brighter on hover

Social icons (Brumble, FLOB, Gigharborly): → subtle glow and slight scale on hover

IMPORTANT: All hover effects must be consistent, clean and not exaggerated.

ACTIVE STATE (VERY IMPORTANT)

Navigation elements must clearly show when they are active (current page).

This applies to:

Header navigation footer left

Behavior:

Active links should remain highlighted (eg green color and/or subtle underline) Users should always clearly see which page they are currently on

IMPORTANT: Active and hover states must be visually consistent across the entire website.

ANIMATIONS / MICRO INTERACTIONS

The website should not feel static.

We would like subtle and professional animations, such as:

smooth transitions between elements minimal background movement (very subtle) soft UI interactions

IMPORTANT: No heavy, flashy or distracting animations.

The goal is a high-end, enterprise-level feel.

COUNTERS / KEY METRICS

We want animated key numbers, for example:

150+ clients 10+ years experience 24/7 support 99.9% uptime

Behavior:

numbers should count up when they come into view (on scroll) fast and smoothly (approx. 0. 5–1 seconds) animation should trigger only once

Overall goal: A modern, dynamic and high-quality website with subtle interactions, not a flashy or overloaded design.

Hi everyone,

I have uploaded additional reference files to give you a clearer idea of the direction we are aiming for.

IMPORTANT: These files are only meant as inspiration and guidance – they are NOT strict templates that must be copied 1:1.

What we particularly like:

Dark / black + green design Subtle grid / tech background (as seen in the PowerPoint) Clean, modern and professional enterprise IT style Structured layout (no one-page scrolling) LANGUAGE FLAGS (IMPORTANT UPDATE)

Please adjust the language selection as follows:

Order:

German (DE) English (EN) Polish (PL)

For ENGLISH: We do NOT want a standard flag.

Instead, please create a combined UK/US flag:

Diagonally split design One side showing the UK flag The other side showing the US flag

This should look clean and professional (not playful).

FOOTER (IMPORTANT)

Footer should be:

Minimal and clean (not large or heavy) Positioned at the very bottom

Include:

Legal Notice / Imprint / Privacy Policy / Data Protection / Terms and Conditions / Terms

And: © Trelvo UG

Social icons:

Brumble FLOB Gigharborly

Please remove:

Pawstream Chirply Snapmoor LAYOUT NOTE

Please avoid duplicate sections (eg "About Us" appearing multiple times).

We prefer a clean and structured layout with clear sections.

Thank you very much – looking forward to your designs!

Ich brauche zusätzliche Tage um durchzusehen

Target Market(s)

Enterprise and mid-sized companies, especially in automotive, finance, technology and IT infrastructure environments.

Industry/Entity Type

IT Consulting / Managed Services / Enterprise IT

Coding

Coded - Design and coding required

Font styles to use
Sans Serif

Colors
0094D4
00A9DD
6FCCEA
C7EBF8
E9F6FB
00AB8E
00BBA5
67D7C9
C6EFE9
E9F9F6
59FF00
82FF00
B8FF75
E3FFCB
F4FFEA

Requirements
Must have
• - Fully coded WordPress website (not just design) - Self-hosted, no dependency on designer - Responsive (desktop, tablet, mobile) - Multilingual (German, English, Polish) - Editable without developer - Clean, modern enterprise design - Structured navigation with subpages (no one-page website) - GDPR-compliant contact form - Scalable structure for future company expansion (group structure)
Nice to have
• - Subtle modern animations (not overloaded) - Mega menu or structured dropdown navigation - Clean icon set and optional illustrations - Reusable page templates - Fast loading performance - SEO-friendly structure - Team presentation with profiles (management, internal staff, technical roles) - Integration of social links (Brumble, Flob, Gigharborly)
Should not have
• - No one-page scrolling website - No overly colorful or playful design - No outdated or generic templates - No confusing or complex navigation - No cheap-looking stock-heavy layouts - No dependency on proprietary builders or subscriptions

```html
<!DOCTYPE html>
<html lang="en">
<head>
<meta charset="utf-8">
<title>Trelvo – Enterprise Data Center Solutions</title>
<link rel="stylesheet" href="https://fonts.googleapis.com/css2?family=Space+Grotesk:wght@400;500;600;700&family=Inter:wght@400;500;600;700&display=swap">
<style>
:root{
  --bg:#121212;
  --bg-deep:#0b0b0b;
  --band:#161616;
  --card:#1a1a1a;
  --card-black:#000;
  --panel:#2a2a2a;
  --line:#2e2e2e;
  --green:#59ff00;
  --green-soft:#b8ff75;
  --green-mid:#82ff00;
  --text:#ffffff;
  --muted:#a3a3a3;
  --dim:#7a7a7a;
  --alert:#ff6a4d;
  --head:'Space Grotesk',sans-serif;
  --body:'Inter',sans-serif;
}
*{box-sizing:border-box;margin:0;padding:0}
html,body{width:1200px;height:3976px;overflow:hidden;background:var(--bg);color:var(--text);font-family:var(--body)}
.page{position:relative;width:1200px;height:3976px;overflow:hidden}
.abs{position:absolute}

/* header */
.site-header{position:absolute;top:0;left:0;width:1200px;height:74px;background:var(--bg-deep);border-bottom:1px solid #1f2a16;display:flex;align-items:center;padding:0 45px}
.brand{font-family:var(--head);font-weight:700;font-size:21px;color:var(--green);letter-spacing:-.5px}
.main-nav{position:absolute;left:226px;top:0;height:74px;display:flex;gap:30px;align-items:center;font-size:13px;color:#d0d0d0}
.main-nav a{color:inherit;text-decoration:none;position:relative}
.main-nav a.active{color:var(--green)}
.main-nav a.active::after{content:"";position:absolute;left:0;right:0;bottom:-8px;height:2px;background:var(--green)}
.lang{position:absolute;right:45px;top:21px;height:32px;width:66px;border-radius:16px;background:#1e1e1e;display:flex;align-items:center;gap:8px;padding-left:12px;font-size:11px;font-weight:700}
.lang .flag{width:16px;height:16px;border-radius:50%;background:linear-gradient(135deg,#1f3fa8 50%,#c8102e 50%)}

/* hero */
.hero{position:absolute;top:75px;left:0;width:1200px;height:790px;background:radial-gradient(ellipse 380px 260px at 420px 250px,rgba(89,255,0,.10),transparent 70%),linear-gradient(90deg,rgba(89,255,0,.06),transparent 4%),var(--bg)}
.badge{position:absolute;left:523px;top:252px;width:154px;height:27px;border:1px solid #3a3a3a;background:#0f0f0f;font-size:11px;font-weight:700;letter-spacing:1px;color:var(--green-soft);display:flex;align-items:center;justify-content:center;gap:8px}
.badge i{width:6px;height:6px;border-radius:50%;background:var(--green)}
.hero-title{position:absolute;top:300px;left:0;width:1200px;text-align:center;font-family:var(--head);font-weight:700;font-size:86px;line-height:90px;letter-spacing:-2px}
.hero-title span{display:block;color:var(--green-soft)}
.hero-sub{position:absolute;top:512px;width:1200px;text-align:center;font-size:19px;color:var(--muted)}
.hero-tag{position:absolute;top:554px;width:1200px;text-align:center;font-size:12px;font-weight:700;letter-spacing:1px}
.btn{position:absolute;display:flex;align-items:center;justify-content:center;font-size:12px;font-weight:700;letter-spacing:.8px}
.btn-primary{left:377px;top:616px;width:241px;height:51px;background:linear-gradient(90deg,var(--green-soft),var(--green));color:#143300}
.btn-ghost{left:641px;top:616px;width:181px;height:51px;border:1px solid #2c2c2c;background:#0f0f0f;color:#fff}

/* competencies */
.eyebrow{font-size:12px;letter-spacing:4px;color:var(--green);font-weight:500}
.section-title{font-family:var(--head);font-weight:600;font-size:33px}
.card{position:absolute;top:1056px;height:375px;padding:30px}
.card-wide{left:45px;width:543px;background:var(--card)}
.card-black{background:var(--card-black);width:260px}
.card svg{display:block}
.card h3{font-family:var(--head);font-weight:600;font-size:22px;margin-top:26px}
.card p{font-size:14px;line-height:24px;color:var(--muted);margin-top:16px}
.card-foot{position:absolute;left:30px;right:30px;bottom:30px;display:flex;justify-content:space-between;align-items:center;font-size:11px;color:var(--muted)}
.card-foot.green{color:var(--green);font-weight:700}
.migration{position:absolute;left:45px;top:1454px;width:1109px;height:331px;background:var(--panel);border:1px solid #3a3a3a}
.migration h3{position:absolute;left:45px;top:50px;font-family:var(--head);font-weight:600;font-size:33px}
.migration p{position:absolute;left:45px;top:112px;width:460px;font-size:16px;line-height:27.5px;color:#bcbcbc}
.tag{position:absolute;top:251px;height:30px;background:#141414;border:1px solid #3a3a3a;font-size:11px;color:var(--green-soft);display:flex;align-items:center;padding:0 15px}
.migration-art{position:absolute;left:577px;top:46px;width:487px;height:240px;background:radial-gradient(ellipse at 55% 50%,#3f8a52 0%,#1d4a2b 45%,#0e2418 100%)}

/* strategy band */
.strategy{position:absolute;top:1948px;left:0;width:1200px;height:472px;background:var(--band)}
.col{position:absolute;top:2040px;width:330px}
.col h3{font-family:var(--head);font-weight:600;font-size:27px;line-height:34px}
.col p{font-size:14px;line-height:22.5px;color:#bcbcbc;margin-top:22px}
.check{display:flex;align-items:center;gap:10px;font-size:13px;font-weight:500;margin-top:18px}
.rule{width:90px;height:3px;background:var(--green);margin-top:30px}
.mini{font-size:11px;letter-spacing:1.5px;color:var(--dim);margin-top:24px}
.alert{margin-top:24px;height:47px;border:1px solid #5a2a1e;background:#1f1412;color:var(--alert);font-size:11px;font-weight:700;display:flex;align-items:center;gap:8px;padding-left:16px}

/* case study */
.case{position:absolute;top:2420px;left:0;width:1200px;height:858px;background:var(--bg)}
.case-shape{position:absolute;left:0;top:0}
.proof{position:absolute;left:45px;top:2575px;height:22px;border-left:3px solid var(--green);background:#1e1e1e;padding:0 12px;font-size:11px;letter-spacing:1.5px;color:#cfcfcf;display:flex;align-items:center}
.case h2{position:absolute;left:45px;top:2628px;font-family:var(--head);font-size:46px;line-height:57px;font-weight:600}
.case h2 span{display:block;font-weight:400;color:#bdbdbd}
.stat{position:absolute;top:2826px}
.stat b{display:block;font-family:var(--head);font-size:30px;color:var(--green-soft);font-weight:600}
.stat small{display:block;font-size:10.5px;color:var(--muted);margin-top:4px}
.quote{position:absolute;left:45px;top:2905px;width:510px;border-left:2px solid #3a3a3a;padding-left:24px;font-size:17px;line-height:26.5px;color:#cfcfcf}
.read{position:absolute;left:45px;top:3019px;font-size:11px;font-weight:700;letter-spacing:1px;display:flex;align-items:center;gap:8px}
.case-frame{position:absolute;left:630px;top:2543px;width:523px;height:523px;background:#1a1a1a;padding:15px}
.case-photo{width:100%;height:100%;background:linear-gradient(180deg,#4a4a4a 0%,#7c7c7c 45%,#b5b5b5 70%,#8a8a8a 100%)}

/* cta */
.cta{position:absolute;left:45px;top:3278px;width:1109px;height:333px;background:var(--green);text-align:center;color:#1f6b00}
.cta::after{content:"";position:absolute;right:0;top:0;width:120px;height:120px;background:rgba(255,255,255,.07)}
.cta h2{margin-top:55px;font-family:var(--head);font-weight:700;font-size:44px;color:#1a5200}
.cta p{margin:20px auto 0;width:560px;font-size:16px;line-height:26px;color:#2e8a05}
.cta .btn{position:absolute;left:372px;top:216px;width:367px;height:57px;background:#123d00;color:var(--green);letter-spacing:3px}

/* footer */
.site-footer{position:absolute;top:3703px;left:0;width:1200px;height:273px;background:var(--bg-deep)}
.site-footer .brand{position:absolute;left:45px;top:50px;color:#fff;font-size:17px}
.foot-claim{position:absolute;left:45px;top:86px;font-size:11px;letter-spacing:1.5px;color:var(--dim);line-height:16px}
.foot-col{position:absolute;top:48px;font-size:11px;letter-spacing:1.5px;color:var(--dim);line-height:26px}
.foot-col h4{color:var(--green);font-weight:700;font-size:11px;letter-spacing:1.5px;margin-bottom:0}
.copy{position:absolute;left:45px;top:215px;font-size:10.5px;letter-spacing:1.2px;color:#5a5a5a}
</style>
</head>
<body>
<div class="page">

<header class="site-header">
  <div class="brand">TRELVO</div>
  <nav class="main-nav">
    <a>Home</a><a>Managed Services</a><a>Services</a><a class="active">Solutions</a><a>Projects</a><a>Resources</a><a>Careers</a><a>Company</a><a>Contact</a>
  </nav>
  <div class="lang"><span class="flag"></span>EN</div>
</header>

<section class="hero">
  <div class="badge" style="top:177px"><i></i>SOLUTIONS HUB</div>
  <h1 class="hero-title" style="top:225px">Enterprise Data<span>Center Solutions</span></h1>
  <p class="hero-sub" style="top:437px">Architecting the foundations of modern enterprise scale.</p>
  <p class="hero-tag" style="top:479px">RELIABLE. SCALABLE. SECURE.</p>
  <a class="btn btn-primary" style="top:541px">EXPLORE INFRASTRUCTURE</a>
  <a class="btn btn-ghost" style="top:541px">TECHNICAL SPECS</a>
</section>

<div class="abs eyebrow" style="left:45px;top:935px">CORE COMPETENCIES</div>
<h2 class="abs section-title" style="left:45px;top:958px">Virtualization &amp; Hybrid Infrastructure</h2>

<article class="card card-wide">
  <svg width="34" height="30" viewBox="0 0 34 30" fill="none" stroke="#59ff00" stroke-width="2"><rect x="2" y="7" width="7" height="16"/><rect x="13" y="7" width="7" height="16"/><rect x="24" y="7" width="7" height="16"/><path d="M5.5 2v5M5.5 23v5M16.5 2v5M16.5 23v5M27.5 2v5M27.5 23v5M4 15h3M15 15h3M26 15h3"/></svg>
  <h3>Nexorin vStack</h3>
  <p>Advanced SDDC design and implementation. We optimize your compute resources with industry-leading hypervisor technology for maximum density and uptime.</p>
  <div class="card-foot green"><span>LEGACY MODERNIZATION</span><svg width="16" height="14" viewBox="0 0 16 14" fill="none" stroke="#d0d0d0" stroke-width="1.6"><path d="M1 7h13M9 2l5 5-5 5"/></svg></div>
</article>
<article class="card card-black" style="left:611px">
  <svg width="30" height="28" viewBox="0 0 30 28" fill="none" stroke="#59ff00" stroke-width="2"><rect x="2" y="3" width="26" height="17"/><path d="M15 20v5M9 25h12"/></svg>
  <h3>Valtek Virtual Apps</h3>
  <p>Secure, high-performance delivery of virtual desktops and applications globally.</p>
  <div class="card-foot"><span>VDI EXPERTISE</span><svg width="16" height="14" viewBox="0 0 16 14" fill="none" stroke="#d0d0d0" stroke-width="1.6"><path d="M1 7h13M9 2l5 5-5 5"/></svg></div>
</article>
<article class="card card-black" style="left:894px">
  <svg width="32" height="28" viewBox="0 0 32 28" fill="none" stroke="#59ff00" stroke-width="2"><rect x="2" y="4" width="16" height="8"/><rect x="2" y="16" width="16" height="8"/><path d="M6 8h3M6 20h3M26 3l-4 10h6l-4 11"/></svg>
  <h3>Quadr-X</h3>
  <p>Seamless Fenestra Server integration and cost-effective virtualization scaling.</p>
  <div class="card-foot"><span>CIRRANE READY</span><svg width="16" height="14" viewBox="0 0 16 14" fill="none" stroke="#d0d0d0" stroke-width="1.6"><path d="M1 7h13M9 2l5 5-5 5"/></svg></div>
</article>

<section class="migration">
  <h3>Cloud Migrations</h3>
  <p>Moving mission-critical workloads without downtime. Our proven migration framework ensures data integrity and operational continuity during the shift to hybrid or public cloud environments.</p>
  <span class="tag" style="left:45px">SKYVANE CERTIFIED</span>
  <span class="tag" style="left:179px">CIRRANE EXPERTS</span>
  <div class="migration-art" role="img" aria-label="Illustration of a glowing green network cloud"></div>
</section>

<section class="strategy"></section>
<div class="col" style="left:45px">
  <h3>Infrastructure<br>Modernization</h3>
  <p>We replace rigid, siloed hardware with fluid, software-defined environments. Transition to Hyper-Converged Infrastructure (HCI) to reduce footprint and complexity.</p>
  <div class="check" style="margin-top:36px"><svg width="13" height="13" viewBox="0 0 13 13" fill="none" stroke="#59ff00" stroke-width="1.4"><circle cx="6.5" cy="6.5" r="5.5"/><path d="M4 6.6l1.8 1.8L9 5"/></svg>Resource Consolidation</div>
  <div class="check"><svg width="13" height="13" viewBox="0 0 13 13" fill="none" stroke="#59ff00" stroke-width="1.4"><circle cx="6.5" cy="6.5" r="5.5"/><path d="M4 6.6l1.8 1.8L9 5"/></svg>Automated Provisioning</div>
</div>
<div class="col" style="left:435px">
  <h3>Hybrid Cloud Strategy</h3>
  <p>Balance the agility of public cloud with the control of on-premise infrastructure. We architect seamless bridges for workload portability and unified management.</p>
  <div class="rule"></div>
  <div class="mini">INTEROPERABILITY / SCALABILITY / GOVERNANCE</div>
</div>
<div class="col" style="left:825px">
  <h3>Zero-Trust Security</h3>
  <p>Security is baked into the fabric of the data center. Implementing micro-segmentation and identity-aware access controls at every layer of the stack.</p>
  <div class="alert"><svg width="11" height="12" viewBox="0 0 11 12" fill="none" stroke="#ff6a4d" stroke-width="1.4"><path d="M5.5 1L1 3v3c0 3 2 4.6 4.5 5.5C8 10.6 10 9 10 6V3z"/><path d="M3.6 6l1.4 1.4L7.6 4.8"/></svg>CYBER-RESILIENCE PROTOCOL ENABLED</div>
</div>

<section class="case">
  <svg class="case-shape" width="1200" height="858" viewBox="0 0 1200 858"><polygon points="1080,0 1200,0 1200,760 920,760" fill="#171717"/></svg>
</section>
<div class="proof">PROOF OF CONCEPT</div>
<h2 class="case h2" style="position:absolute;left:45px;top:2628px;font-family:var(--head);font-size:46px;line-height:57px;font-weight:600">Cloud Migration<br>Success:<span style="display:block;font-weight:400;color:#bdbdbd">Global Automotive OEM</span></h2>
<div class="stat" style="left:45px"><b>2,400+</b><small>VMS MIGRATED</small></div>
<div class="stat" style="left:322px"><b>35%</b><small>OPEX REDUCTION</small></div>
<blockquote class="quote">"Trelvo's technical depth turned a high-risk migration into a strategic advantage. Their zero-downtime methodology was flawless."</blockquote>
<a class="read">READ FULL TECHNICAL WHITE PAPER <svg width="16" height="12" viewBox="0 0 16 12" fill="none" stroke="#59ff00" stroke-width="1.8"><path d="M1 6h13M9 1l5 5-5 5"/></svg></a>
<div class="case-frame"><div class="case-photo" role="img" aria-label="Black and white photo of robotic arms assembling a car in a server hall"></div></div>

<section class="cta">
  <h2>Ready to Modernize Your Infrastructure?</h2>
  <p>Connect with our lead architects for a comprehensive evaluation of your current data center landscape.</p>
  <a class="btn">SCHEDULE A TECHNICAL DEEP-DIVE</a>
</section>

<footer class="site-footer">
  <div class="brand">TRELVO</div>
  <p class="foot-claim">ENGINEERING RELIABLE DATA CENTER<br>FUTURES FOR THE ENTERPRISE TIER.</p>
  <div class="foot-col" style="left:781px"><h4>SOLUTIONS</h4>DATA CENTER<br>CLOUD STRATEGY<br>SECURITY</div>
  <div class="foot-col" style="left:942px"><h4>LEGAL</h4>IMPRINT<br>PRIVACY<br>TERMS</div>
  <div class="foot-col" style="left:1042px"><h4>NETWORK</h4>BRUMBLE<br>FLOB<br>GIGHARBORLY</div>
  <p class="copy">© 2024 TRELVO ENTERPRISE IT CONSULTING. ALL RIGHTS RESERVED.</p>
</footer>

</div>
</body>
</html>
```